http://www.lanternfieldcollective.org/

would like someone to rebuild this -http://www.lanternfieldcollective.com/ to be more modern and more easily updated

Industry/Entity Type

Non Profit

Coding

Coded - Design and coding required

Colors

Designer to choose colors to be used in the design.

Requirements
Must have
• use of the logo, and a newer design for wordpress to be hosted on Azure and easily updated templates

```html
<!DOCTYPE html>
<html lang="en">
<head>
<meta charset="utf-8">
<title>Lanternfield Collective</title>
<link href="https://fonts.googleapis.com/css2?family=Open+Sans:wght@400;600;700&family=Cinzel:wght@400;700&display=swap" rel="stylesheet">
<style>
:root{
  --sky:#3bb5ea;
  --ink:#2a2a2a;
  --muted:#666;
  --grey-bg:#f4f5f7;
  --line:#d7d7d7;
  --footer:#2f3a45;
  --footer-deep:#29333d;
  --navy:#1f2a5c;
}
*{margin:0;padding:0;box-sizing:border-box}
html,body{width:1200px;height:2692px;overflow:hidden}
body{position:relative;font-family:"Open Sans",Arial,sans-serif;color:var(--ink);background:#fff}
.abs{position:absolute}
a{color:inherit;text-decoration:none}

.topbar{left:0;top:0;width:1200px;height:6px;background:var(--sky)}
.call-tab{left:923px;top:0;width:277px;height:42px;background:var(--sky);border-bottom-left-radius:22px;color:#fff;font-size:12px;display:flex;align-items:center;padding-left:26px;gap:6px}
.brand{left:100px;top:60px;display:flex;align-items:center;gap:12px}
.brand-dot{width:34px;height:34px;border-radius:50%;background:var(--navy)}
.brand-name{font-size:21px;font-weight:600;color:var(--navy);letter-spacing:.5px}
.nav{left:458px;top:100px;width:542px;display:flex;align-items:center;justify-content:space-between;font-size:11.5px;font-weight:400;color:#222;white-space:nowrap}
.nav span.sep{color:#444}
.donate{left:1016px;top:92px;width:86px;height:34px;border:2px solid var(--sky);color:var(--sky);font-size:12px;font-weight:400;display:flex;align-items:center;justify-content:center}

.hero{left:0;top:167px;width:1200px;height:529px;background:radial-gradient(ellipse at 55% 55%,#f6c248 0%,#e29a23 35%,#a35a12 70%,#5a300c 100%)}
.hero-box{left:331px;top:327px;width:539px;height:207px;background:rgba(70,60,50,.55);text-align:center;color:#fff}
.hero-box h1{font-family:"Cinzel",Georgia,serif;font-weight:400;font-size:37px;margin-top:22px;letter-spacing:.5px}
.hero-box .sub-name{font-family:"Cinzel",Georgia,serif;font-size:30px;margin-top:6px}
.hero-box p{font-size:16px;margin-top:10px}
.hero-btn{left:527px;top:514px;width:145px;height:39px;background:var(--sky);color:#fff;font-size:14px;display:flex;align-items:center;justify-content:center}
.arrow{width:36px;height:36px;border-radius:50%;background:rgba(60,40,20,.5);display:flex;align-items:center;justify-content:center}

.about{left:0;top:696px;width:1200px;height:532px;background:var(--grey-bg)}
.section-title{width:1200px;text-align:center;font-size:33px;font-weight:600;color:#555}
.about-sub{top:110px;width:1200px;text-align:center;font-size:14px;color:#555}
.cards{left:98px;top:165px;display:flex;gap:11px}
.card{width:243px;height:293px;background:#fff;border:1px solid #cfcfcf;text-align:center;padding:40px 14px 0}
.card svg{height:64px}
.card h3{font-size:17px;font-weight:400;color:#444;margin-top:14px;letter-spacing:.4px}
.card p{font-size:12px;line-height:22px;color:#555;margin-top:8px;height:66px;overflow:hidden}
.card .more{display:block;margin-top:9px;font-size:12px;color:var(--sky)}

.emblem{left:100px;top:1303px;width:593px;height:378px;background:linear-gradient(135deg,#e6e8ec,#fafafa 55%,#e9ebee)}
.quote{left:648px;top:1477px;width:456px;height:275px;background:var(--sky);color:#fff;font-size:14.5px;font-weight:600;line-height:24.6px;padding:26px 24px 0 29px}

.articles{left:0;top:1822px;width:1200px;height:511px;background:var(--grey-bg)}
.article{top:149px;width:489px;height:293px;background:#fff;border:1px solid #cfcfcf}
.article .photo{left:0;top:33px;width:228px;height:225px}
.article .body{left:247px;top:31px;width:222px}
.article h4{font-size:15px;font-weight:400;letter-spacing:.3px}
.article p{font-size:12px;line-height:20.6px;color:#555;margin-top:8px}
.article .btn{display:inline-block;margin-top:14px;background:var(--sky);color:#fff;font-size:11.5px;font-weight:600;padding:9px 11px}

.footer{left:0;top:2333px;width:1200px;height:280px;background:var(--footer);color:#fff}
.footer h5{font-size:15px;font-weight:600}
.contact-row{display:flex;font-size:12px;gap:10px;align-items:flex-start}
.contact-row b{font-weight:600;min-width:52px}
.links li{list-style:none;font-size:12px;border-bottom:1px dotted #55616d;padding:7px 0 8px 18px;position:relative;width:198px}
.links li::before{content:"";position:absolute;left:2px;top:13px;width:5px;height:5px;border-radius:50%;background:var(--sky)}
.socials{display:flex;gap:10px}
.socials span{width:28px;height:28px;border-radius:50%;background:#fff;display:flex;align-items:center;justify-content:center}
.socials span::after{content:"";width:10px;height:10px;border-radius:2px;background:var(--footer)}
.sub-form{width:247px;height:34px;border:1px solid #6c7782;display:flex;align-items:center;justify-content:space-between;padding:0 3px 0 9px;font-size:11px;color:#aab}
.sub-form span{background:var(--sky);color:#fff;font-size:10.5px;padding:6px 5px}
.bottom{left:0;top:2613px;width:1200px;height:79px;background:var(--footer-deep);color:#fff;font-size:12px}
.to-top{left:1066px;top:2640px;width:34px;height:34px;background:#1c242c;display:flex;align-items:center;justify-content:center}
</style>
</head>
<body>

<div class="abs topbar"></div>
<div class="abs call-tab">
  <svg width="11" height="11" viewBox="0 0 24 24"><path fill="#fff" d="M6.6 10.8a15 15 0 0 0 6.6 6.6l2.2-2.2c.3-.3.7-.4 1-.2 1.1.4 2.3.6 3.6.6.6 0 1 .4 1 1V20c0 .6-.4 1-1 1A17 17 0 0 1 3 4c0-.6.4-1 1-1h3.5c.6 0 1 .4 1 1 0 1.3.2 2.5.6 3.6.1.3 0 .7-.2 1z"/></svg>
  <span>Call Us: 1 (555) 014-2290</span>
</div>

<header>
  <div class="abs brand"><span class="brand-dot"></span><span class="brand-name">Lanternfield Collective</span></div>
  <nav class="abs nav">
    <a>HOME</a><span class="sep">|</span><a>ABOUT US</a><span class="sep">|</span><a>PROJECTS</a><span class="sep">|</span><a>NEWSLETTERS &amp; REPORTS</a><span class="sep">|</span><a>MEDIA</a><span class="sep">|</span><a>CONTACT US</a>
  </nav>
  <a class="abs donate">DONATION</a>
</header>

<section class="abs hero" role="img" aria-label="Two hands reaching toward each other against a golden sunset sky"></section>
<div class="abs arrow" style="left:8px;top:394px"><svg width="12" height="12" viewBox="0 0 12 12"><path d="M8 1 3 6l5 5" stroke="#caa" stroke-width="2" fill="none"/></svg></div>
<div class="abs arrow" style="left:1153px;top:393px"><svg width="12" height="12" viewBox="0 0 12 12"><path d="m4 1 5 5-5 5" stroke="#caa" stroke-width="2" fill="none"/></svg></div>
<div class="abs hero-box">
  <h1>LANTERNFIELD COLLECTIVE</h1>
  <div class="sub-name">Lanternfield</div>
  <p>Helping the needy Christian families</p>
</div>
<a class="abs hero-btn">April 2019 Letters</a>

<section class="abs about">
  <h2 class="abs section-title" style="top:50px">ABOUT US</h2>
  <p class="abs about-sub">May God protect and lead in peace our 118th shepherd,&nbsp; Father Elias Marron.</p>
  <div class="abs cards">
    <article class="card">
      <svg viewBox="0 0 70 64" width="70"><path fill="#3bb5ea" d="M35 22c-4-9-16-7-16 2 0 7 9 12 16 18 7-6 16-11 16-18 0-9-12-11-16-2z"/><path fill="#3bb5ea" d="M2 24l8-3 10 22 10 6v15H20L4 44zM68 24l-8-3-10 22-10 6v15h10l16-20z"/></svg>
      <h3>OUR GOAL</h3>
      <p>Is to feed 50 more families a day from your remnants and to add a smile to their faces.</p>
      <a class="more">READ MORE</a>
    </article>
    <article class="card">
      <svg viewBox="0 0 70 64" width="70"><circle cx="37" cy="32" r="27" fill="none" stroke="#3bb5ea" stroke-width="4"/><path d="M37 16v17l10 7" stroke="#3bb5ea" stroke-width="4" fill="none"/><path fill="#3bb5ea" d="M2 30h16l-8 10z"/><rect x="12" y="24" width="8" height="8" fill="#fff"/></svg>
      <h3>HISTORY</h3>
      <p>Today the majority of the problems that face our youngest children, boys and girls in Egypt are caused by lack</p>
      <a class="more">READ MORE</a>
    </article>
    <article class="card">
      <svg viewBox="0 0 70 64" width="70"><rect x="18" y="3" width="36" height="56" rx="3" fill="none" stroke="#3bb5ea" stroke-width="3"/><path d="M25 14h22M25 22h22M25 30h22M25 38h22M25 46h14" stroke="#3bb5ea" stroke-width="2.5"/></svg>
      <h3>PROJECTS</h3>
      <p>Lorem Ipsum is simply dummy text of the printing and typesetting industry. Lorem Ipsum has been the industry's</p>
      <a class="more">READ MORE</a>
    </article>
    <article class="card">
      <svg viewBox="0 0 70 64" width="70"><path d="M8 38l34-26 6 28-28 4z" fill="none" stroke="#3bb5ea" stroke-width="3" stroke-linejoin="round"/><path d="M18 44l4 14h7l-3-15" fill="none" stroke="#3bb5ea" stroke-width="3"/><path d="M55 14l6-6M58 24h8M52 6l2-5" stroke="#3bb5ea" stroke-width="3"/></svg>
      <h3>NEWSLETTERS</h3>
      <p>Lorem Ipsum is simply dummy text of the printing and typesetting industry. Lorem Ipsum has been the industry's</p>
      <a class="more">READ MORE</a>
    </article>
  </div>
</section>

<div class="abs emblem" role="img" aria-label="Circular organisation emblem on a pale geometric triangle backdrop"></div>
<blockquote class="abs quote">Then the King will say to those on His right hand, ‘Come, you blessed of My Father, inherit the kingdom prepared for you from the foundation of the world: &nbsp;for I was hungry and you gave Me food; I was thirsty and you gave Me drink; I was a stranger and you took Me in; &nbsp;I was naked and you clothed Me; I was sick and you visited Me; I was in prison and you came to Me.’ “Assuredly, I say to you, inasmuch as you did it to one of the least of these My brethren, you did it to Me.”</blockquote>

<section class="abs articles">
  <h2 class="abs section-title" style="top:60px">RECENT ARTICLES</h2>
  <article class="abs article" style="left:98px">
    <div class="abs photo" role="img" aria-label="Church leader in ornate gold vestments" style="background:linear-gradient(160deg,#8a6a3a,#c9a060 45%,#5a3d22)"></div>
    <div class="abs body">
      <h4>ARTICLE TITLE HERE</h4>
      <p>Lorem Ipsum is simply dummy text of the printing and typesetting industry. Lorem Ipsum has been the industry's standard dummy text ever since the 1500s, when an unknown printer took a galley of type and scrambled it to make a type specimen book.</p>
      <a class="btn">READ MORE</a>
    </div>
  </article>
  <article class="abs article" style="left:614px">
    <div class="abs photo" role="img" aria-label="Family seated inside a modest home" style="background:linear-gradient(160deg,#6d7684,#9aa2ac 45%,#2e3542)"></div>
    <div class="abs body">
      <h4>ARTICLE TITLE HERE</h4>
      <p>Lorem Ipsum is simply dummy text of the printing and typesetting industry. Lorem Ipsum has been the industry's standard dummy text ever since the 1500s, when an unknown printer took a galley of type and scrambled it to make a type specimen book.</p>
      <a class="btn">READ MORE</a>
    </div>
  </article>
</section>

<footer class="abs footer">
  <h5 class="abs" style="left:101px;top:48px">CONTACT US</h5>
  <div class="abs" style="left:101px;top:103px;display:flex;flex-direction:column;gap:20px">
    <div class="contact-row"><svg width="10" height="14" viewBox="0 0 10 14"><path fill="#3bb5ea" d="M5 0a5 5 0 0 0-5 5c0 4 5 9 5 9s5-5 5-9a5 5 0 0 0-5-5zm0 7a2 2 0 1 1 0-4 2 2 0 0 1 0 4z"/></svg><b>Address:</b><span>P.O. Box 41820<br>Maplebrook, Ohio 44021-1820</span></div>
    <div class="contact-row"><svg width="14" height="14" viewBox="0 0 24 24"><path fill="#3bb5ea" d="M6.6 10.8a15 15 0 0 0 6.6 6.6l2.2-2.2c.3-.3.7-.4 1-.2 1.1.4 2.3.6 3.6.6.6 0 1 .4 1 1V20c0 .6-.4 1-1 1A17 17 0 0 1 3 4c0-.6.4-1 1-1h3.5c.6 0 1 .4 1 1 0 1.3.2 2.5.6 3.6.1.3 0 .7-.2 1z"/></svg><b>Phone:</b><span>1 (555) 014-2290</span></div>
    <div class="contact-row"><svg width="15" height="11" viewBox="0 0 15 11"><rect width="15" height="11" fill="#3bb5ea"/><path d="M0 0l7.5 6L15 0" stroke="#2f3a45" fill="none"/></svg><b>E-mail:</b><span>info@lanternfieldcollective.org</span></div>
  </div>

  <h5 class="abs" style="left:521px;top:48px">QUICK LINKS</h5>
  <ul class="abs links" style="left:522px;top:84px">
    <li>HOME</li><li>ABOUT US</li><li>PROJECTS</li><li>NEWSLETTERS &amp; REPORTS</li><li>CONTACT US</li>
  </ul>

  <h5 class="abs" style="left:969px;top:48px">STAY CONNECTED</h5>
  <div class="abs socials" style="left:958px;top:90px" aria-label="Social profile links"><span></span><span></span><span></span><span></span></div>
  <h5 class="abs" style="left:906px;top:155px;font-size:14px">SUBSCRIBE TO OUR ARTICLES</h5>
  <div class="abs sub-form" style="left:853px;top:186px">Enter Your Email Address<span>SUBSCRIBE</span></div>
  <svg class="abs" style="left:589px;top:280px" width="20" height="9" viewBox="0 0 20 9"><path d="M0 0h20L10 9z" fill="#2f3a45"/></svg>
</footer>
<div class="abs bottom"><p class="abs" style="left:101px;top:35px">Copyright © lanternfieldcollective 2019 - All Rights Reserved</p></div>
<a class="abs to-top"><svg width="14" height="9" viewBox="0 0 14 9"><path d="M1 8l6-6 6 6" stroke="#fff" stroke-width="2" fill="none"/></svg></a>

</body>
</html>
```